Photographer website

This website will contain information to sell the services of marvello tebani an up and coming photographer based in london

Target Market(s)

SME's for corporate head shots
mums for kids parties
actors - for headshots
up and coming models

Industry/Entity Type

Photographer

Number of Pages Required

3 page

Requirements
Must have
• Home
• About me
• Contact me
• Portfolio or gallery

```html
<!DOCTYPE html>
<html lang="en">
<head>
<meta charset="utf-8">
<title>Marvello Tebani – Photographer</title>
<link rel="stylesheet" href="https://fonts.googleapis.com/css2?family=Jost:wght@400;500&family=Parisienne&family=Yanone+Kaffeesatz:wght@400&display=swap">
<style>
  :root {
    --red: #d10a0f;
    --ink: #1a1a1a;
    --text: #333;
    --page: #f6f6f6;
    --nav: #161616;
    --footer: #1d1d1d;
    --footer-bottom: #121212;
    --rule: #c4c4c4;
    --ornament: #cfcfcf;
    --white: #fff;
  }
  * { box-sizing: border-box; margin: 0; padding: 0; }
  html, body { width: 1200px; height: 2903px; overflow: hidden; }
  body { position: relative; background: var(--page); font-family: "Jost", sans-serif; color: var(--text); }
  .abs { position: absolute; }

  /* header */
  .topbar { left: 0; top: 0; width: 1200px; height: 37px; background: var(--red); }
  .topbar .phone { left: 160px; top: 7px; color: var(--white); font-size: 17px; display: flex; align-items: center; gap: 8px; white-space: nowrap; }
  .topbar .social { right: 164px; top: 5px; display: flex; gap: 8px; }
  .topbar .social span { width: 26px; height: 26px; border: 2px solid var(--white); border-radius: 50%; }
  .navbar { left: 0; top: 37px; width: 1200px; height: 60px; background: var(--nav); opacity: .92; z-index: 2; }
  .nav-link { top: 20px; color: var(--white); font-size: 14px; white-space: nowrap; }
  .nav-link.active { border: 1px solid var(--red); padding: 3px 11px; top: 16px; }
  .brand-badge { left: 494px; top: -52px; width: 213px; height: 213px; border-radius: 50%; background: var(--white); z-index: 3; display: flex; align-items: flex-end; justify-content: center; padding-bottom: 58px; box-shadow: 0 2px 8px rgba(0,0,0,.25); }
  .brand-badge span { font-size: 19px; font-weight: 500; color: var(--ink); text-align: center; line-height: 1.15; }

  .hero { left: 0; top: 37px; width: 1200px; height: 532px; background: linear-gradient(100deg, #8c8451 0%, #b7a878 30%, #6f6a3b 60%, #a79a63 100%); }
  .hero-name { right: 80px; top: 480px; font-family: "Yanone Kaffeesatz", sans-serif; font-size: 46px; color: var(--white); white-space: nowrap; }

  /* section headings */
  .section-title { left: 0; width: 1200px; display: flex; justify-content: center; align-items: center; gap: 18px; font-family: "Parisienne", cursive; font-weight: 400; font-size: 38px; color: var(--ink); white-space: nowrap; }
  .section-title em { font-style: normal; color: var(--red); }
  .flourish { display: block; width: 80px; height: 16px; background: var(--ornament); border-radius: 8px; }
  .divider { left: 162px; width: 878px; height: 4px; background: var(--rule); }

  .about-text { left: 232px; top: 686px; width: 736px; text-align: center; font-size: 13.5px; line-height: 24px; color: var(--text); }

  .service { width: 172px; text-align: center; }
  .service .photo { width: 172px; height: 172px; border-radius: 50%; border: 3px solid #444; }
  .service p { margin-top: 18px; font-size: 17px; line-height: 20px; color: var(--ink); }

  .tabs { left: 0; top: 1312px; width: 1200px; display: flex; justify-content: center; gap: 36px; font-size: 13px; color: var(--ink); white-space: nowrap; }
  .tabs .active { color: var(--red); border-bottom: 2px solid var(--red); padding: 0 6px 4px; }

  .btn { background: var(--red); color: var(--white); font-size: 15px; display: flex; align-items: center; justify-content: center; white-space: nowrap; }

  .photographer { width: 202px; height: 223px; }
  .photographer.featured { background: #1e1f16; color: var(--white); text-align: center; padding-top: 44px; }
  .photographer.featured h3 { font-family: "Yanone Kaffeesatz", sans-serif; font-weight: 400; font-size: 24px; }
  .photographer.featured p { font-size: 12px; line-height: 17px; margin: 10px 28px 0; }
  .photographer.featured .btn { width: 86px; height: 28px; font-size: 12px; margin: 12px auto 0; }
  .corner { width: 22px; height: 22px; border-color: var(--red); border-style: solid; }

  /* footer */
  .footer { left: 0; top: 2606px; width: 1200px; height: 258px; background: var(--footer); color: #bdbdbd; }
  .footer-brand { left: 162px; top: 64px; font-size: 28px; font-weight: 500; color: var(--white); display: flex; align-items: center; gap: 10px; white-space: nowrap; }
  .footer-brand i { width: 14px; height: 14px; border-radius: 50%; background: var(--white); display: block; }
  .footer-about { left: 162px; top: 150px; width: 430px; font-size: 11.5px; line-height: 19px; }
  .footer-head { top: 56px; color: var(--white); font-size: 19px; }
  .footer-rule { top: 92px; height: 1px; background: #4a4a4a; }
  .footer-rule b { display: block; width: 40px; height: 1px; background: var(--red); }
  .footer-list { top: 112px; list-style: none; font-size: 12px; line-height: 27px; }
  .footer-list li::before { content: "›"; margin-right: 8px; }
  .footer-list li.current { color: var(--red); }
  .join-item { font-size: 12px; display: flex; align-items: center; gap: 10px; white-space: nowrap; }
  .join-item i { width: 11px; height: 11px; background: #cfcfcf; display: block; }
  .footer-bottom { left: 0; top: 2864px; width: 1200px; height: 39px; background: var(--footer-bottom); color: #9a9a9a; font-size: 12px; }
  .footer-bottom span { white-space: nowrap; }
</style>
</head>
<body>

<!-- header -->
<div class="abs hero" role="img" aria-label="Hero photograph of a woman in a light dress standing in a sunlit meadow"></div>
<div class="abs hero-name">Marvello Tebani</div>

<div class="abs topbar">
  <div class="abs phone">
    <svg width="15" height="15" viewBox="0 0 24 24" aria-hidden="true"><path d="M6.6 10.8a15 15 0 0 0 6.6 6.6l2.2-2.2a1 1 0 0 1 1-.25 11.4 11.4 0 0 0 3.6.57 1 1 0 0 1 1 1V20a1 1 0 0 1-1 1A17 17 0 0 1 3 4a1 1 0 0 1 1-1h3.5a1 1 0 0 1 1 1c0 1.25.2 2.45.57 3.6a1 1 0 0 1-.25 1z" fill="#fff"/></svg>
    +44 20 7946 0321
  </div>
  <div class="abs social" aria-label="Social links"><span></span><span></span><span></span><span></span></div>
</div>

<nav class="abs navbar">
  <a class="abs nav-link active" style="left:222px">Home</a>
  <a class="abs nav-link" style="left:354px">About Me</a>
  <a class="abs nav-link" style="left:784px">Gallery</a>
  <a class="abs nav-link" style="left:888px">Contact Me</a>
</nav>
<div class="abs brand-badge"><span>Marvello<br>Tebani</span></div>

<!-- about -->
<h2 class="abs section-title" style="top:620px">
  <span class="flourish" role="img" aria-label="Decorative scroll ornament"></span>
  <span>About <em>Marvello Tebani</em></span>
  <span class="flourish" role="img" aria-label="Decorative scroll ornament"></span>
</h2>
<p class="abs about-text">Lorem ipsum dolor sit amet, consectetuer adipiscing elit, sed diam nonummy nibh euismod tincidunt ut laoreet dolore magna aliquam erat volutpat. Ut wisi enim ad minim veniam, quis nostrud exerci tation ullamcorper suscipit lobortis nisl ut aliquip ex ea commodo consequat. Duis autem vel eum iriure dolor in hendrerit in vulputate velit esse molestie consequat, vel illum dolore eu feugiat nulla facilisis at vero eros et accumsan et iusto odio dignissim qui blandit praesent luptatum zzril delenit augue duis dolore te feugait nulla facilisi.</p>

<div class="abs divider" style="top:851px" role="img" aria-label="Decorative wavy divider"></div>

<!-- services -->
<div class="abs service" style="left:160px;top:911px"><div class="photo" role="img" aria-label="Portrait of a smiling businessman in a suit" style="background:linear-gradient(160deg,#6f8a55,#2d3a2a)"></div><p>Corporate<br>Head Shots</p></div>
<div class="abs service" style="left:394px;top:911px"><div class="photo" role="img" aria-label="Mother and daughter smiling together" style="background:linear-gradient(160deg,#c9b7a8,#b3272c)"></div><p>Mums For<br>Kids Parties</p></div>
<div class="abs service" style="left:634px;top:911px"><div class="photo" role="img" aria-label="Headshot of a young actor" style="background:linear-gradient(160deg,#8f959a,#5a4b42)"></div><p>Actors For<br>Headshots</p></div>
<div class="abs service" style="left:866px;top:911px"><div class="photo" role="img" aria-label="Model with jewelled headpiece" style="background:linear-gradient(160deg,#e9c7cc,#8c1f3a)"></div><p>Upcoming<br>Models</p></div>

<div class="abs divider" style="top:1198px" role="img" aria-label="Decorative wavy divider"></div>

<!-- gallery -->
<h2 class="abs section-title" style="top:1246px">
  <span class="flourish" role="img" aria-label="Decorative scroll ornament"></span>
  <span>Photo <em>Gallery</em></span>
  <span class="flourish" role="img" aria-label="Decorative scroll ornament"></span>
</h2>
<div class="abs tabs"><span class="active">All</span><span>Corporate Head Shots</span><span>Mums For Kids Parties</span><span>Actors For Headshots</span><span>Upcoming Models</span></div>

<div class="abs" style="left:162px;top:1358px;width:502px;height:202px;background:linear-gradient(120deg,#5d7a3e,#c7b39a,#7e5d4a)" role="img" aria-label="Group of friends smiling at an outdoor gathering"></div>
<div class="abs" style="left:685px;top:1358px;width:355px;height:310px;background:linear-gradient(160deg,#8d8a80,#2d4a73,#b8232a)" role="img" aria-label="Young man in a blazer and hat seated against a stone wall"></div>
<div class="abs" style="left:162px;top:1583px;width:254px;height:194px;background:linear-gradient(120deg,#3b3433,#c9a18c,#4a3f3c)" role="img" aria-label="Close beauty portrait with dramatic makeup"></div>
<div class="abs" style="left:439px;top:1583px;width:225px;height:194px;background:linear-gradient(150deg,#f0eceb,#cfc5c6,#8b5d5a)" role="img" aria-label="Mother and daughter in white dresses"></div>
<div class="abs" style="left:685px;top:1693px;width:355px;height:310px;background:linear-gradient(160deg,#e6dac1,#b98a5a,#6f4a32)" role="img" aria-label="Woman with a flower crown among blossoms"></div>
<div class="abs" style="left:162px;top:1801px;width:502px;height:202px;background:linear-gradient(120deg,#2a2a2a,#cfcfcf,#5d5d5d)" role="img" aria-label="Black and white portrait of a smiling couple"></div>

<div class="abs btn" style="left:528px;top:2043px;width:142px;height:36px">View All Photos</div>

<div class="abs divider" style="top:2134px" role="img" aria-label="Decorative wavy divider"></div>

<!-- photographers -->
<h2 class="abs section-title" style="top:2183px">
  <span class="flourish" role="img" aria-label="Decorative scroll ornament"></span>
  <span>Upcoming <em>Photographer</em></span>
  <span class="flourish" role="img" aria-label="Decorative scroll ornament"></span>
</h2>

<div class="abs photographer featured" style="left:162px;top:2254px">
  <h3>Rafe Colman</h3>
  <p>Ut wisi enim ad minim veniam, quis nostrud exerci tation ullamcorper</p>
  <div class="btn">View Detail</div>
</div>
<div class="abs corner" style="left:162px;top:2254px;border-width:3px 0 0 3px"></div>
<div class="abs corner" style="left:342px;top:2254px;border-width:3px 3px 0 0"></div>
<div class="abs corner" style="left:162px;top:2455px;border-width:0 0 3px 3px"></div>
<div class="abs corner" style="left:342px;top:2455px;border-width:0 3px 3px 0"></div>
<div class="abs photographer" style="left:387px;top:2254px;background:linear-gradient(160deg,#c8b070,#3a3a3a)" role="img" aria-label="Young woman holding a camera outdoors"></div>
<div class="abs photographer" style="left:611px;top:2254px;background:linear-gradient(160deg,#e8e4df,#3a2d2a)" role="img" aria-label="Woman looking down at a camera"></div>
<div class="abs photographer" style="left:836px;top:2254px;background:linear-gradient(160deg,#9fb5c9,#7a6a55)" role="img" aria-label="Man with a professional video camera"></div>

<div class="abs btn" style="left:507px;top:2517px;width:186px;height:36px">View All Photographers</div>

<!-- footer -->
<footer class="abs footer">
  <div class="abs footer-brand"><i></i>Marvello Tebani</div>
  <p class="abs footer-about">Lorem ipsum dolor sit amet, consectetuer adipiscing elit, sed diam nonummy nibh euismod tincidunt ut laoreet dolore magna aliquam erat volutpat. Ut wisi enim ad minim veniam, quis nostrud exerci tation ullamcorper suscipit lobortis nisl ut aliquip ex ea commodo consequat.</p>

  <div class="abs footer-head" style="left:660px">Company</div>
  <div class="abs footer-rule" style="left:660px;width:98px"><b></b></div>
  <ul class="abs footer-list" style="left:660px">
    <li class="current">Home</li><li>About Me</li><li>Gallery</li><li>Contact Me</li>
  </ul>

  <div class="abs footer-head" style="left:832px">Join Us</div>
  <div class="abs footer-rule" style="left:832px;width:208px"><b></b></div>
  <div class="abs join-item" style="left:832px;top:116px"><i></i>Friendbook</div>
  <div class="abs join-item" style="left:832px;top:149px"><i></i>Chirper</div>
  <div class="abs join-item" style="left:832px;top:182px"><i></i>WorkLink</div>
  <div class="abs join-item" style="left:832px;top:215px"><i></i>ViewTube</div>
  <div class="abs join-item" style="left:950px;top:116px"><i></i>Circles+</div>
  <div class="abs join-item" style="left:950px;top:149px"><i></i>Snapgram</div>
  <div class="abs join-item" style="left:950px;top:182px"><i></i>RSSFeed</div>
  <div class="abs join-item" style="left:950px;top:215px"><i></i>Callspace</div>
</footer>
<div class="abs footer-bottom">
  <span class="abs" style="left:162px;top:12px">© 2016 MarvelloTebani.com. All Rights Reserved.</span>
  <span class="abs" style="left:838px;top:12px">Terms &amp; Condition</span>
  <span class="abs" style="left:964px;top:12px">Privacy Policy</span>
</div>

</body>
</html>
```